PAWS postcard design

We need a design for a non profit organization associated with an animal shelter called PAWS of HBRPC. HBRPC stands for Hollybrook Valley Regional Pet Center. This 501c3 group provides assistance to the community in the form of training, consultation, financial assistance, education and more. Our goal is to provide options to people in need to help them keep their pets rather than surrender them to the shelter. We have a logo already but we need something for people to take away and to use as a handout. Need to include phone numbers and website, which I will provide.

Target Market(s)

general public who have pets

Industry/Entity Type

Non Profit

Font styles to use
Sans Serif
Other font styles liked:
• designer can choose others

Requirements
Must have
• The logo must be fairly large. Colors should be bright and eye-pleasing. Like colors that match the logo. Easy to read fonts. Pics of animals are OK but no pics with people. Not too much text, short and to the point.
Nice to have
• not sure
Should not have
• No pics with people. Not black and white. Not too much text.

```html
<!DOCTYPE html>
<html lang="en">
<head>
<meta charset="utf-8">
<title>PAWS of HBRPC – Postcard</title>
<link rel="stylesheet" href="https://fonts.googleapis.com/css2?family=Lilita+One&family=Arimo:wght@400;700&display=swap">
<style>
  :root{
    --sun:#fbf01c;
    --sky:#23bde6;
    --ocean:#1f6fc4;
    --cherry:#e22b26;
    --red-box:#d90d12;
    --ink:#0b0b0b;
    --paper:#ffffff;
    --stage:#d9d9d9;
    --fur:#c99a5e;
    --fur-light:#e8c89a;
    --tabby:#9a8472;
  }
  *{box-sizing:border-box;margin:0;padding:0}
  html,body{width:1200px;height:902px;overflow:hidden;background:var(--stage)}
  .postcard{
    position:absolute;left:40px;top:143px;width:1120px;height:616px;
    overflow:hidden;background:var(--sun);
    font-family:"Arimo",Arial,sans-serif;
  }
  .postcard__backdrop{position:absolute;inset:0;width:100%;height:100%}

  .brand{
    position:absolute;left:40px;top:120px;width:300px;
    display:flex;flex-direction:column;align-items:center;gap:40px;
  }
  .brand__dot{width:86px;height:86px;border-radius:50%;background:var(--paper)}
  .brand__name{font-family:"Arimo",Arial,sans-serif;font-weight:700;font-size:34px;color:var(--ink);white-space:nowrap}

  .headline{
    position:absolute;left:530px;width:560px;text-align:center;
    font-family:"Lilita One",sans-serif;text-transform:uppercase;line-height:1;
  }
  .headline--top{top:38px;font-size:56px;color:var(--cherry)}
  .headline--sub{top:106px;font-size:45px;color:var(--sky)}

  .photo{position:absolute}
  .photo--cat-frame{
    left:383px;top:172px;width:182px;height:182px;border-radius:50%;
    background:var(--paper);border:6px solid var(--sun);
    box-shadow:0 0 0 3px var(--ocean) inset;
  }
  .photo--cat{
    position:absolute;left:12px;top:12px;width:146px;height:146px;border-radius:50%;
    background:radial-gradient(circle at 50% 45%,#b7a594,var(--tabby) 60%,#eee 100%);
  }
  .photo--puppy{
    left:812px;top:172px;width:226px;height:205px;border-radius:46% 46% 30% 30%;
    background:radial-gradient(ellipse at 50% 45%,var(--fur-light),var(--fur) 75%);
  }
  .photo--dog{
    left:10px;top:326px;width:216px;height:272px;border-radius:44% 44% 18% 18%;
    background:radial-gradient(ellipse at 50% 40%,#dcae6e,var(--fur) 70%);
  }

  .services__title{
    position:absolute;left:384px;top:396px;width:200px;text-align:center;
    font-family:"Lilita One",sans-serif;font-size:21px;color:var(--cherry);
  }
  .services__intro{
    position:absolute;left:292px;top:428px;font-size:18.5px;font-weight:700;color:var(--sky);
  }
  .services__list{
    position:absolute;left:292px;top:462px;width:420px;list-style:none;
    display:grid;grid-template-columns:185px 235px;row-gap:9px;
    font-size:17.5px;font-weight:700;color:var(--ink);
  }
  .services__list li{position:relative;padding-left:25px}
  .services__list li::before{
    content:"";position:absolute;left:3px;top:6px;width:8px;height:8px;border-radius:50%;
    background:var(--cherry);
  }

  .contact{
    position:absolute;left:733px;top:347px;width:369px;height:218px;
    background:var(--red-box);border:2px solid #f5b8b8;
    box-shadow:2px 3px 8px rgba(0,0,0,.45);text-align:center;color:var(--paper);
  }
  .contact__label{margin-top:55px;font-family:"Lilita One",sans-serif;font-size:22px}
  .contact__phone{
    margin:8px auto 0;width:258px;height:40px;border-radius:20px;
    background:var(--sun);color:var(--ink);font-size:27px;font-weight:400;line-height:40px;
    box-shadow:0 2px 3px rgba(0,0,0,.35);
  }
  .contact__web{margin-top:12px;font-size:17.5px;font-weight:700}
  .contact__social{
    margin-top:14px;display:flex;justify-content:center;align-items:center;gap:8px;
    font-size:15px;font-weight:700;
  }
  .contact__network{font-size:15px;font-weight:700;color:var(--paper)}
  .contact__square{width:18px;height:18px;background:var(--ocean)}
</style>
</head>
<body>
<main class="postcard">
  <svg class="postcard__backdrop" viewBox="0 0 1120 616" preserveAspectRatio="none" aria-hidden="true">
    <rect width="1120" height="616" fill="var(--sun)"/>
    <path d="M0 380 Q200 330 430 300 Q700 268 1120 312 L1120 520 Q500 555 0 470 Z" fill="var(--paper)"/>
    <path d="M430 250 Q700 215 1120 262 L1120 300 Q700 255 430 290 Z" fill="var(--ink)"/>
    <path d="M430 290 Q700 255 1120 300 L1120 312 Q700 268 430 302 Z" fill="var(--sky)"/>
    <path d="M0 470 Q500 555 1120 510 L1120 522 Q500 567 0 482 Z" fill="var(--ocean)"/>
    <path d="M0 482 Q500 567 1120 522 L1120 534 Q500 579 0 494 Z" fill="var(--sun)"/>
    <path d="M0 494 Q500 579 1120 534 L1120 616 L0 616 Z" fill="var(--ink)"/>
    <circle cx="190" cy="140" r="300" fill="var(--sun)"/>
    <circle cx="190" cy="140" r="290" fill="var(--cherry)"/>
    <circle cx="190" cy="140" r="284" fill="var(--paper)"/>
    <circle cx="190" cy="140" r="278" fill="var(--sky)"/>
  </svg>

  <div class="brand">
    <span class="brand__dot" aria-hidden="true"></span>
    <span class="brand__name">PAWS of HBRPC</span>
  </div>

  <h1 class="headline headline--top">Hollybrook Valley</h1>
  <h2 class="headline headline--sub">Regional Pet Center</h2>

  <div class="photo photo--cat-frame">
    <div class="photo--cat" role="img" aria-label="Photo of a tabby cat lying down"></div>
  </div>
  <div class="photo photo--puppy" role="img" aria-label="Photo of a golden retriever puppy resting its paws on the contact box"></div>
  <div class="photo photo--dog" role="img" aria-label="Photo of a golden labrador lying down"></div>

  <section class="services">
    <h3 class="services__title">WE PROVIDES</h3>
    <p class="services__intro">Assistance to the community in the form of</p>
    <ul class="services__list">
      <li>Training</li>
      <li>Financial assistance</li>
      <li>Consultation</li>
      <li>Education and more</li>
    </ul>
  </section>

  <aside class="contact">
    <p class="contact__label">CALL US</p>
    <p class="contact__phone">0198 552 734</p>
    <p class="contact__web">Visit Us: www.hollybrookpaws.org</p>
    <p class="contact__social">Follow Us On <span class="contact__network">PawBook</span><span class="contact__square" aria-hidden="true"></span></p>
  </aside>
</main>
</body>
</html>
```